Photography Business, Business Card

Looking for a unique cutting edge card that takes advantage of the latest printing technologies. Please review this site for all the options they office: https://plumeprints.example. If you can think it they can do it. And if you have an idea and do not know if they can do it, I will check into it.
Updates

Target Market(s)

People and places I took images of and future clients.

Industry/Entity Type

Photography

Contact Information for Business Card

Name, cell & email. Colin Hartley, chartley@kvnphoto.example, 318-742-9061

Colors

Designer to choose only greyscale colors for use in the design.

Requirements
Must have
• 100% cutting edge. Is so great, those I hand it to always show it to someone else. A piece of art.
Nice to have
• Blacks, silvers, greys, some red. Maybe other colors?

```html
<!DOCTYPE html>
<html lang="en">
<head>
<meta charset="utf-8">
<title>KVN Photography – Business Card</title>
<link href="https://fonts.googleapis.com/css2?family=Ubuntu:wght@400;500;700&family=Ubuntu+Condensed&display=swap" rel="stylesheet">
<style>
  :root{
    --stage:#1d211e;
    --red:#e8202a;
    --white:#ffffff;
    --ink:#2b2b2e;
    --card-black:#151517;
    --card-black-soft:#1f1f22;
    --grey:#8a8a8e;
  }
  *{box-sizing:border-box;margin:0;padding:0}
  html,body{width:1200px;height:900px;overflow:hidden}
  body{
    background:var(--stage);
    font-family:"Ubuntu",sans-serif;
    position:relative;
  }
  .card{
    position:absolute;
    width:560px;height:320px;
    border-radius:22px;
    border:2px solid var(--red);
    overflow:hidden;
  }

  /* ---------- back card ---------- */
  .card-back{left:320px;top:70px;background:var(--card-black)}
  .card-back .shade{
    position:absolute;left:0;right:0;bottom:0;height:90px;
    background:var(--card-black-soft);
  }
  .card-back .brand{
    position:absolute;left:0;right:0;top:78px;text-align:center;
  }
  .brand-name{
    font-weight:700;color:var(--red);letter-spacing:4px;
    font-size:64px;line-height:1;
  }
  .tagline{
    font-family:"Ubuntu Condensed",sans-serif;
    color:var(--red);font-size:21px;margin-top:10px;
  }
  .card-back .web{
    position:absolute;left:0;right:0;top:242px;
    display:flex;justify-content:center;align-items:center;gap:12px;
    color:#c9c9cc;font-size:16px;
  }

  /* edge dots */
  .dots{position:absolute;right:-14px;top:14px;display:flex;flex-direction:column;gap:14px}
  .dots span{display:block;width:28px;height:28px;border-radius:50%;background:var(--red)}

  /* ---------- front card ---------- */
  .card-front{left:320px;top:470px;background:var(--white)}
  .front-logo{
    position:absolute;left:0;top:0;width:232px;height:100%;
    display:flex;flex-direction:column;justify-content:center;align-items:center;
  }
  .front-logo .brand-name{font-size:56px}
  .front-logo .tagline{font-size:19px}
  .divider{position:absolute;left:232px;top:0;width:2px;height:100%;background:var(--red)}

  .name-band{
    position:absolute;left:234px;top:26px;width:290px;height:72px;
    background:var(--red);border-radius:0 16px 16px 0;
    display:flex;align-items:center;gap:14px;padding-left:18px;
    color:var(--white);
  }
  .name-band .mark{width:42px;height:42px;border-radius:6px;background:#6d6d71}
  .person{font-size:25px;font-weight:700;line-height:1}
  .role{font-size:10px;letter-spacing:6px;margin-top:5px}

  .contacts{position:absolute;left:262px;top:122px;list-style:none}
  .contacts li{
    display:flex;align-items:center;gap:14px;
    height:42px;font-size:15px;font-weight:500;color:var(--ink);
  }
  .icon{width:28px;height:28px;flex:none}
</style>
</head>
<body>

<section class="card card-back" aria-label="Business card back">
  <div class="shade"></div>
  <div class="dots"><span></span><span></span><span></span></div>
  <div class="brand">
    <div class="brand-name">KVN</div>
    <div class="tagline">Creative Visual Services</div>
  </div>
  <div class="web">
    <svg class="icon" viewBox="0 0 28 28" aria-hidden="true"><circle cx="14" cy="14" r="13" fill="var(--red)"/><circle cx="14" cy="14" r="7.5" fill="none" stroke="#fff" stroke-width="1.6"/><path d="M6.5 14h15M14 6.5c-3.5 4-3.5 11 0 15M14 6.5c3.5 4 3.5 11 0 15" fill="none" stroke="#fff" stroke-width="1.4"/></svg>
    <span>www.kvnphoto.example</span>
  </div>
</section>

<section class="card card-front" aria-label="Business card front">
  <div class="front-logo">
    <div class="brand-name">KVN</div>
    <div class="tagline">Creative Visual Services</div>
  </div>
  <div class="divider"></div>
  <div class="dots"><span></span><span></span><span></span></div>

  <div class="name-band">
    <span class="mark"></span>
    <div>
      <div class="person">Colin Hartley</div>
      <div class="role">PHOTOGRAPHY</div>
    </div>
  </div>

  <ul class="contacts">
    <li>
      <svg class="icon" viewBox="0 0 28 28" aria-hidden="true"><circle cx="14" cy="14" r="13" fill="var(--red)"/><path d="M10 8c1 0 2.5 2.8 2.5 3.5S11 13 11.3 13.8c.7 1.5 1.6 2.4 2.9 3 .8.3 1.4-1.3 2.2-1.3s3.6 1.5 3.6 2.5-1.5 2.3-2.6 2.3C12.8 20.3 7.7 15.2 7.7 10.5 7.7 9.4 9 8 10 8z" fill="#fff"/></svg>
      <span>+318 742 9061</span>
    </li>
    <li>
      <svg class="icon" viewBox="0 0 28 28" aria-hidden="true"><circle cx="14" cy="14" r="13" fill="var(--red)"/><circle cx="14" cy="14" r="7.5" fill="none" stroke="#fff" stroke-width="1.6"/><path d="M6.5 14h15M14 6.5c-3.5 4-3.5 11 0 15M14 6.5c3.5 4 3.5 11 0 15" fill="none" stroke="#fff" stroke-width="1.4"/></svg>
      <span>www.kvnphoto.example</span>
    </li>
    <li>
      <svg class="icon" viewBox="0 0 28 28" aria-hidden="true"><circle cx="14" cy="14" r="13" fill="var(--red)"/><rect x="7.5" y="9.5" width="13" height="9" rx="1" fill="#fff"/><path d="M7.8 10l6.2 5 6.2-5" fill="none" stroke="var(--red)" stroke-width="1.4"/></svg>
      <span>chartley@kvnphoto.example</span>
    </li>
    <li>
      <svg class="icon" viewBox="0 0 28 28" aria-hidden="true"><circle cx="14" cy="14" r="13" fill="var(--red)"/><path d="M14 21.5s-5.5-5.6-5.5-9.3a5.5 5.5 0 0 1 11 0c0 3.7-5.5 9.3-5.5 9.3z" fill="#fff"/><circle cx="14" cy="12.2" r="2" fill="var(--red)"/></svg>
      <span>Lorem ip.Elm Str. 6A</span>
    </li>
  </ul>
</section>

</body>
</html>
```